The Festival! Poster for an Annual Dance Showcase

We are looking for a dynamic festival/concert style poster for our annual dance showcase featuring at least one image of our dancers and the main information. The main image should be one of the dancers but there can be a collage of the dancers or smaller images around the poster. I have included some reference images but it can vary from them.

Must have this information;
Date - May 22-26
Location - Mabel Corwin Hale Theatre
Tickets - Vondo.bm

Target Market(s)

Parents and people who love dance

Industry/Entity Type

Dance

Font styles to use
Sans Serif

Colors
E54698
E96AAD
F1A4CE
F9D9EA
FCEFF6

Requirements
Must have
• Logo, Date and Location, Picture of Dancer

```html
<!DOCTYPE html>
<html lang="en">
<head>
<meta charset="utf-8">
<title>Annual Dance Showcase – Festivals</title>
<link href="https://fonts.googleapis.com/css2?family=Montserrat:wght@600;700;800;900&family=Oswald:wght@300;400;500;600&display=swap" rel="stylesheet">
<style>
  :root {
    --page: #ffffff;
    --tan: #d6af95;
    --coral: #e8735a;
    --ticket: #e3d4a8;
    --ticket-ink: #4a4036;
    --peach: #edd3bb;
    --royal: #2753b5;
    --magenta: #c42b84;
    --teal: #89aab1;
    --navy: #232b44;
    --white: #ffffff;
  }
  html, body {
    margin: 0;
    width: 1200px;
    height: 1200px;
    overflow: hidden;
    background: var(--page);
  }
  .canvas {
    position: relative;
    width: 1200px;
    height: 1200px;
  }
  .poster {
    position: absolute;
    left: 203px;
    top: 40px;
    width: 793px;
    height: 1120px;
    display: block;
  }
  .headline-annual { font-family: "Montserrat", sans-serif; font-weight: 800; fill: var(--white); }
  .headline-sub { font-family: "Oswald", sans-serif; font-weight: 400; fill: var(--white); }
  .festival-word { font-family: "Montserrat", sans-serif; font-weight: 900; fill: var(--white); }
  .ticket-text { font-family: "Oswald", sans-serif; font-weight: 400; fill: var(--ticket-ink); }
  .school-name { font-family: "Montserrat", sans-serif; font-weight: 700; fill: var(--white); }
  .school-sub { font-family: "Montserrat", sans-serif; font-weight: 600; fill: var(--white); }
  .venue { font-family: "Montserrat", sans-serif; font-weight: 800; fill: var(--white); }
  .dates { font-family: "Oswald", sans-serif; font-weight: 600; fill: var(--navy); }
</style>
</head>
<body>
<div class="canvas">
  <svg class="poster" viewBox="0 0 1020 1440" xmlns="http://www.w3.org/2000/svg">
    <defs>
      <linearGradient id="photo-nude" x1="0" y1="0" x2="0" y2="1">
        <stop offset="0" stop-color="#e2c0a4"/>
        <stop offset="1" stop-color="#c8a084"/>
      </linearGradient>
      <linearGradient id="photo-blue" x1="0" y1="0" x2="1" y2="1">
        <stop offset="0" stop-color="#3763c2"/>
        <stop offset="1" stop-color="#1f4399"/>
      </linearGradient>
      <linearGradient id="photo-pair" x1="0" y1="0" x2="0" y2="1">
        <stop offset="0" stop-color="#e3c2a6"/>
        <stop offset="0.5" stop-color="#8a7366"/>
        <stop offset="1" stop-color="#3a3134"/>
      </linearGradient>
    </defs>

    <rect class="page-bg" x="0" y="0" width="1020" height="1440" fill="var(--white)"/>

    <!-- colour blocks -->
    <rect class="block-tan" x="0" y="0" width="290" height="645" fill="var(--tan)"/>
    <rect class="block-coral" x="313" y="0" width="707" height="295" fill="var(--coral)"/>
    <rect class="block-peach" x="573" y="310" width="447" height="840" fill="var(--peach)"/>
    <rect class="block-royal" x="0" y="663" width="551" height="345" fill="var(--royal)"/>
    <rect class="block-magenta" x="0" y="1026" width="551" height="125" fill="var(--magenta)"/>
    <rect class="block-teal" x="0" y="1172" width="1020" height="268" fill="var(--teal)"/>

    <!-- dancer photo areas -->
    <rect class="photo-dancer-nude" role="img" aria-label="Photo of a dancer in a flowing nude dress, arched back with one arm raised"
      x="30" y="50" width="240" height="540" rx="14" fill="url(#photo-nude)"/>
    <rect class="photo-dancer-blue" role="img" aria-label="Photo of a dancer in a royal blue gown in a low lunge with arms over her head"
      x="150" y="620" width="350" height="385" rx="14" fill="url(#photo-blue)"/>
    <rect class="photo-dancers-pair" role="img" aria-label="Photo of two dancers in black mesh skirts and embroidered tops, arms extended"
      x="600" y="340" width="400" height="790" rx="14" fill="url(#photo-pair)"/>

    <!-- headline -->
    <text class="headline-annual" x="345" y="136" font-size="132" textLength="632" lengthAdjust="spacingAndGlyphs">ANNUAL</text>
    <text class="headline-sub" x="345" y="250" font-size="104" textLength="634" lengthAdjust="spacingAndGlyphs">DANCE SHOWCASE</text>

    <!-- ticket stub -->
    <g class="ticket">
      <path d="M320 318 h230 v335 h-230 z" fill="var(--ticket)"/>
      <circle cx="320" cy="318" r="22" fill="var(--white)"/>
      <circle cx="550" cy="318" r="22" fill="var(--white)"/>
      <circle cx="320" cy="653" r="22" fill="var(--white)"/>
      <circle cx="550" cy="653" r="22" fill="var(--white)"/>
      <line x1="320" y1="480" x2="550" y2="480" stroke="var(--white)" stroke-width="3" stroke-dasharray="10 6"/>
      <text class="ticket-text" x="435" y="440" font-size="72" text-anchor="middle" textLength="175" lengthAdjust="spacingAndGlyphs">TICKETS</text>
      <text class="ticket-text" x="435" y="575" font-size="72" text-anchor="middle" textLength="175" lengthAdjust="spacingAndGlyphs">VONDO.BM</text>
    </g>

    <!-- vertical festival word -->
    <text class="festival-word" transform="translate(188 970) rotate(-90)" x="0" y="0" font-size="190" textLength="930" lengthAdjust="spacingAndGlyphs">Festivals</text>

    <!-- school name -->
    <g class="school-mark">
      <circle cx="125" cy="1088" r="20" fill="var(--white)"/>
      <text class="school-name" x="165" y="1085" font-size="42" textLength="280" lengthAdjust="spacingAndGlyphs">NEW STRIDE</text>
      <text class="school-sub" x="165" y="1118" font-size="26" textLength="280" lengthAdjust="spacingAndGlyphs">SCHOOL OF DANCE</text>
    </g>

    <!-- venue and dates -->
    <text class="venue" x="40" y="1298" font-size="76" textLength="664" lengthAdjust="spacingAndGlyphs">MABEL CORWIN</text>
    <text class="venue" x="40" y="1383" font-size="76" textLength="664" lengthAdjust="spacingAndGlyphs">HALE THEATRE</text>
    <line class="divider" x1="740" y1="1208" x2="740" y2="1414" stroke="var(--white)" stroke-width="4"/>
    <text class="dates" x="882" y="1313" font-size="128" text-anchor="middle" textLength="196" lengthAdjust="spacingAndGlyphs">MAY</text>
    <text class="dates" x="882" y="1402" font-size="104" text-anchor="middle" textLength="196" lengthAdjust="spacingAndGlyphs">22-26</text>
  </svg>
</div>
</body>
</html>
```